Business cards, letterheads, envelopes, notepad design

We are a new business in Miami, Florida. We produce business printing, signs and photogifts such as canvas prints, t shirts, mugs, phone cases etc.
Our store will be very modern with interactive stations for clients to design their own products on our cloud design software. We want something that will appeal to business clients and the general public clients.
We need designs for business cards, letterheads, notepads, and envelopes - all 4 colour process - full bleed OK.

Target Market(s)

We target both business clients and the general public.

Industry/Entity Type

Store

Font styles to use
Sans Serif
Other font styles liked:
• Harabara

Colors
acd036
33a6d7
e34197
000000

Requirements
Must have
• Cyan, Magenta, Lime Green
Should not have
• No cats. Absolutely.

```html
<!DOCTYPE html>
<html lang="en">
<head>
<meta charset="utf-8">
<title>Copyhue Stationery Set</title>
<link rel="stylesheet" href="https://fonts.googleapis.com/css2?family=Open+Sans:wght@400;600;700&family=Dancing+Script:wght@500&display=swap">
<style>
  :root {
    --lime: #acd036;
    --lime-light: #c4e25a;
    --cyan: #33a6d7;
    --cyan-light: #52bde8;
    --magenta: #e34197;
    --magenta-light: #ef63ad;
    --ink: #1a1a1a;
    --text: #444;
    --paper: #ffffff;
    --board: #1c1c1c;
    --window: #e6e6e6;
  }
  * { box-sizing: border-box; margin: 0; padding: 0; }
  html, body { width: 1200px; height: 900px; overflow: hidden; }
  body {
    background: var(--board);
    font-family: "Open Sans", Arial, sans-serif;
    position: relative;
    color: var(--text);
  }
  .piece { position: absolute; overflow: hidden; }

  /* brand wordmark */
  .brand {
    font-family: "Open Sans", Arial, sans-serif;
    font-weight: 700;
    color: var(--ink);
    letter-spacing: -0.5px;
    line-height: 1;
    white-space: nowrap;
  }

  /* tri-colour stripe */
  .stripe { position: absolute; left: 0; right: 0; bottom: 0; height: 10px; display: flex; }
  .stripe span { flex: 1; }
  .stripe .s-lime { background: var(--lime); }
  .stripe .s-cyan { background: var(--cyan); }
  .stripe .s-magenta { background: var(--magenta); }

  /* coloured backs */
  .back-lime { background: radial-gradient(circle at 50% 45%, var(--lime-light), var(--lime) 75%); }
  .back-cyan { background: radial-gradient(circle at 50% 45%, var(--cyan-light), var(--cyan) 75%); }
  .back-magenta { background: radial-gradient(circle at 50% 45%, var(--magenta-light), var(--magenta) 75%); }
  .back .brand {
    position: absolute; left: 0; right: 0; text-align: center;
  }
  .back .url {
    position: absolute; left: 0; right: 0; text-align: center;
    color: #fff; font-size: 6px;
  }

  /* contact line */
  .contacts { display: flex; justify-content: center; gap: 5px; font-size: 5.5px; color: var(--text); white-space: nowrap; }
  .contacts .item { display: inline-flex; align-items: center; gap: 2px; }
  .dot { width: 4px; height: 4px; border-radius: 50%; display: inline-block; }
  .dot-m { background: var(--magenta); }
  .dot-c { background: var(--cyan); }
  .dot-l { background: var(--lime); }
  .address { font-size: 5.5px; text-align: center; color: var(--text); }

  /* letterhead */
  .letterhead { left: 26px; top: 27px; width: 269px; height: 382px; background: var(--paper); }
  .letterhead .brand { position: absolute; top: 58px; left: 0; right: 0; text-align: center; font-size: 24px; }
  .letter-body { position: absolute; left: 13px; top: 100px; width: 244px; font-size: 4.6px; line-height: 1.45; color: #555; }
  .letter-body p { margin-bottom: 5px; }
  .signature { position: absolute; left: 13px; top: 290px; font-family: "Dancing Script", cursive; font-size: 10px; color: #555; }
  .sign-role { position: absolute; left: 13px; top: 303px; font-size: 4.6px; color: #555; }
  .letterhead .address { position: absolute; left: 0; right: 0; top: 350px; }
  .letterhead .contacts { position: absolute; left: 0; right: 0; top: 356px; }

  /* folder-size backs */
  .sheet-lime { left: 316px; top: 22px; width: 271px; height: 386px; }
  .sheet-cyan { left: 609px; top: 22px; width: 271px; height: 383px; }
  .sheet-magenta { left: 901px; top: 25px; width: 270px; height: 383px; }
  .sheet .brand { top: 205px; font-size: 36px; }
  .sheet .url { bottom: 17px; }

  /* envelopes */
  .envelope { width: 369px; height: 213px; overflow: visible; }
  .envelope .flap { position: absolute; left: 0; top: 0; width: 369px; height: 50px; }
  .envelope .body { position: absolute; left: 0; top: 47px; width: 369px; height: 166px; background: var(--paper); overflow: hidden; }
  .envelope .brand { position: absolute; left: 20px; top: 47px; font-size: 19px; }
  .envelope .window {
    position: absolute; left: 211px; top: 34px; width: 135px; height: 35px;
    border-radius: 5px; border: 1px solid #c8c8c8;
    background: linear-gradient(#f2f2f2, var(--window));
  }
  .envelope .address { position: absolute; left: 0; right: 0; top: 127px; }
  .envelope .contacts { position: absolute; left: 0; right: 0; top: 134px; }
  .env-magenta { left: 26px; top: 440px; }
  .env-cyan { left: 407px; top: 434px; }
  .env-lime { left: 802px; top: 437px; }

  /* business cards */
  .card-front { left: 29px; top: 685px; width: 271px; height: 153px; background: var(--paper); }
  .card-front .brand { position: absolute; left: 0; right: 0; top: 58px; text-align: center; font-size: 26px; }
  .card-front .name { position: absolute; left: 14px; top: 110px; font-size: 8px; font-weight: 700; color: var(--magenta); }
  .card-front .name .role { color: var(--cyan); font-weight: 400; }
  .card-front .card-address { position: absolute; left: 14px; top: 121px; font-size: 5.5px; }
  .card-front .contacts { position: absolute; left: 14px; top: 129px; justify-content: flex-start; }
  .card { width: 273px; height: 156px; }
  .card .brand { top: 62px; font-size: 30px; }
  .card .url { bottom: 12px; }
  .card-lime { left: 314px; top: 682px; }
  .card-magenta { left: 606px; top: 682px; width: 274px; }
  .card-cyan { left: 895px; top: 682px; width: 276px; }
</style>
</head>
<body>

  <!-- Letterhead -->
  <section class="piece letterhead" aria-label="Letterhead">
    <div class="brand">Copyhue</div>
    <div class="letter-body">
      <p>Dear Customer,<br>Thank you for choosing our studio for your recent print order. We are pleased to confirm that your business cards, letterheads and envelopes are now in production on our four colour press. Each sheet is checked by hand before packing, and we trim every job to full bleed so the colour runs cleanly to the edge of the paper.</p>
      <p>Our new Miami store opens next month with design stations where you can build your own canvas prints, shirts, mugs and phone cases using our cloud software. Staff will be on hand to help with layout, colour matching and proofing, so every piece looks right the first time it leaves the press.</p>
      <p>Your order will be ready for collection within five working days. If you prefer delivery, simply call the number below and we will arrange a time that suits you.</p>
      <p>We look forward to working with you again on signs, banners and photo gifts. Please keep this letter as a record of your order and share any feedback with our team at any time.</p>
    </div>
    <div class="signature">Daniel Reyes</div>
    <div class="sign-role">Company Director</div>
    <div class="address">Address Line 1, State, Zip Code, Country Name</div>
    <div class="contacts">
      <span class="item"><i class="dot dot-m"></i>555-010-20488</span>
      <span class="item"><i class="dot dot-m"></i>555-019-3321</span>
      <span class="item"><i class="dot dot-m"></i>hello@copyhue.example</span>
      <span class="item"><i class="dot dot-m"></i>www.copyhue.example</span>
    </div>
    <div class="stripe"><span class="s-lime"></span><span class="s-cyan"></span><span class="s-magenta"></span></div>
  </section>

  <!-- Sheet backs -->
  <section class="piece back sheet sheet-lime back-lime" aria-label="Lime sheet back">
    <div class="brand">Copyhue</div>
    <div class="url">www.copyhue.example</div>
  </section>
  <section class="piece back sheet sheet-cyan back-cyan" aria-label="Cyan sheet back">
    <div class="brand">Copyhue</div>
    <div class="url">www.copyhue.example</div>
  </section>
  <section class="piece back sheet sheet-magenta back-magenta" aria-label="Magenta sheet back">
    <div class="brand">Copyhue</div>
    <div class="url">www.copyhue.example</div>
  </section>

  <!-- Envelopes -->
  <section class="piece envelope env-magenta" aria-label="Magenta envelope">
    <svg class="flap" viewBox="0 0 369 50" aria-hidden="true">
      <path d="M0,50 L0,38 Q0,22 30,20 L150,10 Q184,2 218,10 L339,20 Q369,22 369,38 L369,50 Z" fill="var(--magenta)"/>
    </svg>
    <div class="body">
      <div class="brand">Copyhue</div>
      <div class="window"></div>
      <div class="address">Address Line 1, State, Zip Code, Country Name</div>
      <div class="contacts">
        <span class="item"><i class="dot dot-m"></i>555-010-20488</span>
        <span class="item"><i class="dot dot-m"></i>555-019-3321</span>
        <span class="item"><i class="dot dot-m"></i>hello@copyhue.example</span>
        <span class="item"><i class="dot dot-m"></i>www.copyhue.example</span>
      </div>
      <div class="stripe"><span class="s-lime"></span><span class="s-cyan"></span><span class="s-magenta"></span></div>
    </div>
  </section>
  <section class="piece envelope env-cyan" aria-label="Cyan envelope">
    <svg class="flap" viewBox="0 0 369 50" aria-hidden="true">
      <path d="M0,50 L0,38 Q0,22 30,20 L150,10 Q184,2 218,10 L339,20 Q369,22 369,38 L369,50 Z" fill="var(--cyan)"/>
    </svg>
    <div class="body">
      <div class="brand">Copyhue</div>
      <div class="window"></div>
      <div class="address">Address Line 1, State, Zip Code, Country Name</div>
      <div class="contacts">
        <span class="item"><i class="dot dot-m"></i>555-010-20488</span>
        <span class="item"><i class="dot dot-m"></i>555-019-3321</span>
        <span class="item"><i class="dot dot-m"></i>hello@copyhue.example</span>
        <span class="item"><i class="dot dot-m"></i>www.copyhue.example</span>
      </div>
      <div class="stripe"><span class="s-lime"></span><span class="s-cyan"></span><span class="s-magenta"></span></div>
    </div>
  </section>
  <section class="piece envelope env-lime" aria-label="Lime envelope">
    <svg class="flap" viewBox="0 0 369 50" aria-hidden="true">
      <path d="M0,50 L0,38 Q0,22 30,20 L150,10 Q184,2 218,10 L339,20 Q369,22 369,38 L369,50 Z" fill="var(--lime)"/>
    </svg>
    <div class="body">
      <div class="brand">Copyhue</div>
      <div class="window"></div>
      <div class="address">Address Line 1, State, Zip Code, Country Name</div>
      <div class="contacts">
        <span class="item"><i class="dot dot-m"></i>555-010-20488</span>
        <span class="item"><i class="dot dot-m"></i>555-019-3321</span>
        <span class="item"><i class="dot dot-m"></i>hello@copyhue.example</span>
        <span class="item"><i class="dot dot-m"></i>www.copyhue.example</span>
      </div>
      <div class="stripe"><span class="s-lime"></span><span class="s-cyan"></span><span class="s-magenta"></span></div>
    </div>
  </section>

  <!-- Business cards -->
  <section class="piece card-front" aria-label="Business card front">
    <div class="brand">Copyhue</div>
    <div class="name">DANIEL REYES <span class="role">| Job Title</span></div>
    <div class="card-address">Address Line 1, State, Zip Code, Country Name</div>
    <div class="contacts">
      <span class="item"><i class="dot dot-m"></i>555-010-20488</span>
      <span class="item"><i class="dot dot-m"></i>555-019-3321</span>
      <span class="item"><i class="dot dot-m"></i>hello@copyhue.example</span>
      <span class="item"><i class="dot dot-m"></i>www.copyhue.example</span>
    </div>
    <div class="stripe"><span class="s-lime"></span><span class="s-cyan"></span><span class="s-magenta"></span></div>
  </section>
  <section class="piece back card card-lime back-lime" aria-label="Lime card back">
    <div class="brand">Copyhue</div>
    <div class="url">www.copyhue.example</div>
  </section>
  <section class="piece back card card-magenta back-magenta" aria-label="Magenta card back">
    <div class="brand">Copyhue</div>
    <div class="url">www.copyhue.example</div>
  </section>
  <section class="piece back card card-cyan back-cyan" aria-label="Cyan card back">
    <div class="brand">Copyhue</div>
    <div class="url">www.copyhue.example</div>
  </section>

</body>
</html>
```